Ward Compass Business Card Design*

We need a business card design for our company Ward Compass. Our company is specialized in providing online consulting services regarding medical institutions, hospitals and doctors. We work with patients worldwide looking to choose between healthcare providers. We have a website you may use as a reference, where we list doctors and clinics worldwide. So we target Medical providers as well as patients worldwide.
Target Market(s)
Medical Providers and patients around the world
Industry/Entity Type
Medical
Contact Information for Business Card
Salma Derkaoui
CEO
+90 612 348 2071
info@wardcompass-example.com
www.wardcompass-example.com
14 Annakhil 3 H.R.B. Rabat, Morocco
Requirements
Must have
- Company logo/name on one full side, personal info and smaller logo and company name on the other side.
Nice to have
- Smart and elegant design

```html
<!DOCTYPE html>
<html lang="en">
<head>
<meta charset="utf-8">
<title>Ward Compass Business Card</title>
<link href="https://fonts.googleapis.com/css2?family=Montserrat:wght@400;600;700&display=swap" rel="stylesheet">
<style>
  :root {
    --backdrop: #7aaac0;
    --navy: #1b2d5e;
    --card-front: #efefef;
    --card-back: #ffffff;
    --grey-text: #6b6b6b;
  }
  * { margin: 0; padding: 0; box-sizing: border-box; }
  html, body { width: 1200px; height: 800px; overflow: hidden; }
  body {
    background: var(--backdrop);
    font-family: "Montserrat", Arial, sans-serif;
    position: relative;
  }
  .card {
    position: absolute;
    width: 520px;
    height: 300px;
    top: 250px;
    overflow: hidden;
    box-shadow: 0 6px 18px rgba(20, 50, 70, 0.25);
  }
  .card--front { left: 50px; background: var(--card-front); }
  .card--back { left: 630px; background: var(--card-back); }

  .brand {
    display: flex;
    align-items: center;
    gap: 10px;
    color: var(--navy);
    font-weight: 700;
    letter-spacing: 0.04em;
  }
  .brand__dot {
    border-radius: 50%;
    background: var(--navy);
  }
  .card--front .brand {
    position: absolute;
    top: 100px;
    left: 0; right: 0;
    justify-content: center;
    font-size: 26px;
  }
  .card--front .brand__dot { width: 34px; height: 34px; }

  .front-band {
    position: absolute;
    left: 0; right: 0;
    top: 215px;
    height: 44px;
    background: var(--navy);
    color: #fff;
    font-size: 9px;
    letter-spacing: 0.25em;
    display: flex;
    align-items: center;
    justify-content: center;
  }

  .corner-tab {
    position: absolute;
    top: 0; right: 0;
    width: 26px; height: 62px;
    background: var(--navy);
  }
  .card--back .brand {
    position: absolute;
    top: 52px;
    right: 46px;
    font-size: 15px;
    gap: 7px;
  }
  .card--back .brand__dot { width: 20px; height: 20px; }

  .name-block {
    position: absolute;
    top: 100px;
    left: 18px;
    width: 262px;
    height: 66px;
    background: var(--navy);
    color: #fff;
    padding: 12px 18px;
  }
  .name-block__name {
    font-size: 22px;
    font-weight: 600;
    letter-spacing: 0.03em;
    line-height: 1.1;
  }
  .name-block__role {
    font-size: 9px;
    letter-spacing: 0.35em;
    margin-top: 4px;
  }

  .contacts {
    position: absolute;
    top: 186px;
    left: 36px;
    list-style: none;
  }
  .contacts::before {
    content: "";
    position: absolute;
    left: 9px; top: 10px; bottom: 10px;
    width: 1px;
    background: var(--navy);
  }
  .contacts__item {
    position: relative;
    display: flex;
    align-items: center;
    gap: 10px;
    height: 24px;
    font-size: 11px;
    color: #333;
    letter-spacing: 0.03em;
  }
  .contacts__icon {
    width: 19px; height: 19px;
    border-radius: 50%;
    background: var(--navy);
    display: flex;
    align-items: center;
    justify-content: center;
    color: #fff;
    font-size: 11px;
    font-weight: 700;
    flex-shrink: 0;
  }
  .back-band {
    position: absolute;
    right: 0;
    bottom: 38px;
    width: 215px;
    height: 42px;
    background: var(--navy);
    color: #fff;
    font-size: 8px;
    letter-spacing: 0.2em;
    display: flex;
    align-items: center;
    justify-content: center;
  }
</style>
</head>
<body>

  <section class="card card--front" aria-label="Card front">
    <div class="brand">
      <span class="brand__dot"></span>
      <span class="brand__name">WARD COMPASS</span>
    </div>
    <div class="front-band">WWW.WARDCOMPASS-EXAMPLE.COM</div>
  </section>

  <section class="card card--back" aria-label="Card back">
    <div class="corner-tab"></div>
    <div class="brand">
      <span class="brand__dot"></span>
      <span class="brand__name">WARD COMPASS</span>
    </div>

    <div class="name-block">
      <p class="name-block__name">SALMA DERKAOUI</p>
      <p class="name-block__role">CEO</p>
    </div>

    <ul class="contacts">
      <li class="contacts__item">
        <span class="contacts__icon">
          <svg width="11" height="11" viewBox="0 0 24 24" fill="#fff"><path d="M6.6 10.8a15.1 15.1 0 0 0 6.6 6.6l2.2-2.2c.3-.3.7-.4 1-.2 1.1.4 2.3.6 3.6.6.6 0 1 .4 1 1V20c0 .6-.4 1-1 1A17 17 0 0 1 3 4c0-.6.4-1 1-1h3.5c.6 0 1 .4 1 1 0 1.3.2 2.5.6 3.6.1.3 0 .7-.2 1z"/></svg>
        </span>
        +90 612 348 2071
      </li>
      <li class="contacts__item">
        <span class="contacts__icon">@</span>
        INFO@WARDCOMPASS-EXAMPLE.COM
      </li>
      <li class="contacts__item">
        <span class="contacts__icon">
          <svg width="12" height="12" viewBox="0 0 24 24" fill="none" stroke="#fff" stroke-width="1.8"><circle cx="12" cy="12" r="9"/><path d="M3 12h18M12 3c3 3 3 15 0 18M12 3c-3 3-3 15 0 18"/></svg>
        </span>
        WWW.WARDCOMPASS-EXAMPLE.COM
      </li>
    </ul>

    <div class="back-band">WWW.WARDCOMPASS-EXAMPLE.COM</div>
  </section>

</body>
</html>
```